Business Card Design for an Investment Company

We need a business card design for our private investment company, called Dunmore Equity. Dunmore Equity is an investments partnership that aims to acquire shares in listed companies with a view to influencing those companies through active dialogue in order to improve their value. We need designs that use the logo colors (blue, grey, white), we need both English and Arabic on the business cards (can be on one side or 2 sides). The final logo should communicate professionalism, conservatism (nothing too fancy or too cheesy), that we are smart, conservative and old school.

Target Market(s)

Investment companies

Industry/Entity Type

Investment

Contact Information for Business Card

Tariq Salmanuddin Farouqi
Senior Executive Officer

Harbor Court 07, Level 3, Office 214/12
QTFZ

+9714987650
tfarouqi@dunmore-equity.com
www.dunmore-equity.com

Requirements
Must have
• Logo to be placed on the left hand side of the business card
• for the Arabic, we only need to have the name and title so it can be accomodated on one side so we can have the other side with full color and logo. The arabic that needs to be used is the below:
• طارق سلمان الدين فاروقي
• المدير التنفيدي

```html
<!DOCTYPE html>
<html lang="en">
<head>
<meta charset="utf-8">
<title>Dunmore Equity – Business Card</title>
<link rel="stylesheet" href="https://fonts.googleapis.com/css2?family=Roboto:wght@400;500;700&family=Noto+Naskh+Arabic:wght@500;700&display=swap">
<style>
  :root {
    --backdrop: #262626;
    --card-white: #f2f2f2;
    --brand-blue: #126a9c;
    --band-grey: #505050;
    --text-dark: #505050;
    --text-light: #f4f4f4;
  }
  * { margin: 0; padding: 0; box-sizing: border-box; }
  html, body { width: 1200px; height: 960px; overflow: hidden; }
  body {
    background: var(--backdrop);
    font-family: "Roboto", Arial, sans-serif;
    position: relative;
  }
  .card {
    position: absolute;
    width: 600px;
    height: 343px;
  }
  .card--front { left: 314px; top: 113px; background: var(--card-white); }
  .card--back { left: 311px; top: 472px; background: var(--brand-blue); }

  .wordmark {
    position: absolute;
    left: 36px;
    font-weight: 700;
    font-size: 42px;
    letter-spacing: -1px;
    line-height: 1;
    white-space: nowrap;
  }
  .card--front .wordmark { top: 68px; color: var(--brand-blue); }
  .card--back .wordmark { top: 146px; color: var(--text-light); font-size: 46px; }

  .arabic-identity {
    position: absolute;
    right: 36px;
    top: 60px;
    text-align: right;
    direction: rtl;
    font-family: "Noto Naskh Arabic", serif;
    color: var(--text-dark);
    line-height: 1.5;
  }
  .arabic-identity__name { font-size: 20px; font-weight: 700; }
  .arabic-identity__title { font-size: 15px; font-weight: 500; }

  .contact-band {
    position: absolute;
    left: 12px; top: 182px;
    width: 575px; height: 148px;
    background: var(--band-grey);
    color: var(--text-light);
    text-align: center;
  }
  .contact-band__name {
    margin-top: 26px;
    font-size: 18px;
    font-weight: 500;
    text-transform: uppercase;
    white-space: nowrap;
  }
  .contact-band__title { font-size: 14px; font-weight: 400; margin-left: 6px; }
  .contact-band__address { margin-top: 8px; font-size: 14.5px; }
  .contact-band__lines {
    margin-top: 6px;
    font-size: 14.5px;
    display: flex;
    justify-content: center;
    gap: 8px;
    white-space: nowrap;
  }
  .contact-band__item { display: inline-flex; align-items: center; gap: 3px; }
  .icon { width: 12px; height: 12px; fill: var(--text-light); }
  .website {
    font-size: 14.5px;
    letter-spacing: 5px;
    text-align: center;
  }
  .contact-band .website { margin-top: 6px; }
  .card--back .website {
    position: absolute;
    left: 0; right: 0; top: 290px;
    color: var(--text-light);
  }
</style>
</head>
<body>
  <section class="card card--front">
    <div class="wordmark">Dunmore Equity</div>
    <div class="arabic-identity" lang="ar">
      <p class="arabic-identity__name">طارق سلمان الدين فاروقي</p>
      <p class="arabic-identity__title">المدير التنفيدي</p>
    </div>
    <div class="contact-band">
      <p class="contact-band__name">Tariq Salmanuddin Farouqi <span class="contact-band__title">- Senior Executive Officer</span></p>
      <p class="contact-band__address">Harbor Court 07, Level 3, Office 214/12, QTFZ</p>
      <p class="contact-band__lines">
        <span class="contact-band__item">
          <svg class="icon" viewBox="0 0 12 12"><path d="M2.5 0.5 L4.5 0.5 L5 3.5 L3.6 4.5 Q4.8 7.2 7.5 8.4 L8.5 7 L11.5 7.5 L11.5 9.5 Q11.5 11.5 9.5 11.5 Q1 10.5 0.5 2.5 Q0.5 0.5 2.5 0.5Z"/></svg>+9714987650</span>
        <span class="contact-band__item">
          <svg class="icon" viewBox="0 0 12 12"><path d="M3 0h6v12H3z M4 1.5v8h4v-8z"/></svg>+9714987651</span>
        <span class="contact-band__item">
          <svg class="icon" viewBox="0 0 12 12"><path d="M3 1h6v3H3z M1 5h10v5H9V8H3v2H1z M3 9h6v3H3z"/></svg>+9714987652</span>
        <span class="contact-band__item">
          <svg class="icon" viewBox="0 0 12 12"><path d="M0.5 2.5h11v7h-11z"/><path d="M0.8 2.8L6 6.8L11.2 2.8" fill="none" stroke="#505050" stroke-width="1"/></svg>tfarouqi@dunmore-equity.com</span>
      </p>
      <p class="website">www.dunmore-equity.com</p>
    </div>
  </section>

  <section class="card card--back">
    <div class="wordmark">Dunmore Equity</div>
    <p class="website">www.dunmore-equity.com</p>
  </section>
</body>
</html>
```